Commercial Real Estate

We need a business card design for a new commercial real estate business that specializes in apartment building brokerage. Not individual units but the entire complex. We find and represent the owners existing buildings and well as new buyers for those buildings. The design should convey trust, integrity, knowledge and growth. It should be easily read.

Target Market(s)

40 to 65 years old

Industry/Entity Type

Real Estate

```html
<!DOCTYPE html>
<html lang="en">
<head>
<meta charset="UTF-8">
<title>Halbrook Realty Group – Business Card</title>
<link href="https://fonts.googleapis.com/css2?family=Arimo:wght@400;700&display=swap" rel="stylesheet">
<style>
  :root {
    --slate: #4b5b5c;
    --teal: #5cbdbb;
    --paper: #e8eaea;
    --white: #f4f6f6;
    --backdrop: #d9dcdc;
  }
  * { margin: 0; padding: 0; box-sizing: border-box; }
  html, body {
    width: 1200px;
    height: 900px;
    overflow: hidden;
    background: var(--backdrop);
    font-family: "Arimo", Arial, sans-serif;
  }
  .canvas {
    width: 1200px;
    height: 900px;
    display: flex;
    flex-direction: column;
    align-items: center;
    justify-content: center;
    gap: 44px;
  }
  .card {
    width: 630px;
    height: 360px;
    position: relative;
    box-shadow: 0 6px 18px rgba(0,0,0,0.18);
    overflow: hidden;
  }

  /* Front */
  .card-front { background: var(--slate); }
  .card-front .brand {
    position: absolute;
    left: 0; right: 0; top: 130px;
    text-align: center;
  }
  .brand-name {
    font-weight: 700;
    font-size: 40px;
    letter-spacing: 3px;
    text-transform: uppercase;
    color: var(--white);
    line-height: 1;
  }
  .brand-rule {
    width: 300px;
    height: 3px;
    background: var(--teal);
    margin: 14px auto 0;
  }
  .card-front .website {
    position: absolute;
    right: 34px; bottom: 30px;
    color: var(--teal);
    font-size: 17px;
    font-weight: 700;
  }

  /* Back */
  .card-back { display: flex; }
  .contact-panel {
    width: 56%;
    background: var(--slate);
    color: var(--white);
    padding: 36px 30px 0 34px;
  }
  .person-name {
    font-size: 24px;
    font-weight: 400;
  }
  .person-title {
    font-size: 13px;
    letter-spacing: 1px;
    margin-left: 8px;
  }
  .contact-list {
    list-style: none;
    margin-top: 18px;
    font-size: 14px;
    line-height: 1.45;
  }
  .contact-list .label {
    color: var(--teal);
    font-weight: 700;
    display: inline-block;
    width: 14px;
  }
  .address {
    font-size: 14px;
    margin-top: 18px;
  }
  .contact-rule {
    width: 240px;
    height: 3px;
    background: var(--teal);
    margin-top: 28px;
  }
  .contact-panel .website {
    display: block;
    margin-top: 14px;
    color: var(--teal);
    font-size: 16px;
    font-weight: 700;
  }
  .brand-panel {
    flex: 1;
    background: var(--paper);
    display: flex;
    flex-direction: column;
    align-items: center;
    justify-content: center;
    padding-top: 60px;
  }
  .brand-panel .brand-name {
    color: var(--slate);
    font-size: 28px;
    letter-spacing: 2px;
    text-align: center;
    line-height: 1.15;
  }
  .brand-panel .brand-rule {
    width: 200px;
    margin-top: 12px;
  }
</style>
</head>
<body>
  <main class="canvas">
    <section class="card card-front" aria-label="Business card front">
      <div class="brand">
        <div class="brand-name">Halbrook Realty</div>
        <div class="brand-rule"></div>
      </div>
      <span class="website">www.halbrookrealty.com</span>
    </section>

    <section class="card card-back" aria-label="Business card back">
      <div class="contact-panel">
        <h1 class="person-name">Daniel Harlow<span class="person-title">MANAGER</span></h1>
        <ul class="contact-list">
          <li><span class="label">T</span> 0400 555 218</li>
          <li><span class="label">F</span> 0400 555 219</li>
          <li><span class="label">E</span> daniel.harlow@halbrookrealty.com</li>
        </ul>
        <p class="address">PO Box 2741 Riverton NT 0830</p>
        <div class="contact-rule"></div>
        <span class="website">www.halbrookrealty.com</span>
      </div>
      <div class="brand-panel">
        <div class="brand-name">Halbrook<br>Realty</div>
        <div class="brand-rule"></div>
      </div>
    </section>
  </main>
</body>
</html>
```